Fundraiser Brochure for Candle Company

We are a mid-sized candle company. We have been doing fundraisers for many years and need a new design/look for our brochure. Please don't design it to mimic our website - I want that updated as well. I'm looking for more of a Marisa Thornbury, Juniper Hollow look. I want this to be 5.5 w X 8.5 h size but that isn't an option here. I called Quick Press Prints and they said to just put it in the notes - OK there ya go!! We do not need an order form with this as we are going to make a separate sheet to insert for the order form. I'd like the products types (barn candles, barn brick sets, reflective light candles, soup) each to have their own page. Rooms Sprays and Diffusers can go on the same page since there are only a few of each to select from. The fragrance descriptions can be all on 1 page since there are repeats in the different product types. The soup is a big seller for us :) Please feel free to do what you'd like to with the pix. I know the quality isn't amazing but it's all I have right now. Thank you!!! Dorinda

Font styles to use
Serif

Requirements
Nice to have
• I listed what I'd like in the project descriptions

```html
<!DOCTYPE html>
<html lang="en">
<head>
<meta charset="utf-8">
<title>Fragrance Descriptions</title>
<link href="https://fonts.googleapis.com/css2?family=Noto+Serif:wght@400;700&display=swap" rel="stylesheet">
<style>
  :root {
    --page-bg: #ffffff;
    --wash-a: #fbe3c6;
    --wash-b: #e2f0fa;
    --wash-c: #e8f4d8;
    --panel-bg: #f3f6d6;
    --panel-glow: #cfe39a;
    --cell-bg: #f6f8e2;
    --code-bg: #d4df2c;
    --band-bg: #8cc63f;
    --band-text: #ffffff;
    --heading-green: #3aa935;
    --rule: #9ccf5a;
    --ink: #2b2b2b;
  }
  * { box-sizing: border-box; margin: 0; padding: 0; }
  html, body { width: 934px; height: 1200px; overflow: hidden; background: var(--page-bg); }
  body { position: relative; font-family: "Noto Serif", Georgia, serif; color: var(--ink); }

  .background-wash {
    position: absolute; inset: 0;
    background:
      radial-gradient(circle at 8% 6%, var(--wash-a), transparent 30%),
      radial-gradient(circle at 96% 10%, var(--wash-b), transparent 32%),
      radial-gradient(circle at 95% 60%, var(--wash-c), transparent 28%),
      radial-gradient(circle at 4% 80%, var(--wash-a), transparent 26%),
      var(--page-bg);
  }

  .fragrance-panel {
    position: absolute; left: 104px; top: 69px; width: 726px; height: 1062px;
    background: var(--panel-bg);
    box-shadow: inset 0 0 14px 6px var(--panel-glow), 0 0 6px var(--panel-glow);
    padding: 0 6px;
  }
  .fragrance-table { width: 100%; border-collapse: collapse; table-layout: fixed; }
  .col-category { width: 178px; }
  .col-code { width: 71px; }
  .fragrance-table th {
    height: 37px; color: var(--heading-green); font-weight: 700; font-size: 14.5px;
    text-transform: uppercase; vertical-align: middle; padding-top: 6px;
  }
  .fragrance-table th.head-category { text-align: center; padding-right: 20px; }
  .fragrance-table th.head-code { text-align: left; padding-left: 7px; }
  .section-band td {
    height: 26px; background: var(--band-bg); color: var(--band-text);
    font-weight: 700; font-size: 17.5px; text-align: center; text-transform: uppercase;
    vertical-align: middle;
  }
  .scent-row td { border-bottom: 1px solid var(--rule); vertical-align: top; font-size: 14.8px; line-height: 19.5px; }
  .scent-row:last-child td { border-bottom: none; }
  .scent-name { padding: 3px 4px 0 6px; background: var(--cell-bg); font-size: 16px !important; }
  .scent-code { background: var(--code-bg); text-align: center; vertical-align: middle !important; font-size: 16px !important; }
  .scent-notes { padding: 0 4px 0 6px; background: var(--cell-bg); hyphens: auto; }
</style>
</head>
<body>

<div class="background-wash" role="img" aria-label="Soft pastel watercolor wash in orange, blue, green and coral behind the fragrance list"></div>

<main class="fragrance-panel">
  <table class="fragrance-table">
    <colgroup><col class="col-category"><col class="col-code"><col></colgroup>
    <thead>
      <tr><th class="head-category">Category</th><th class="head-code">Code</th><th>Description</th></tr>
    </thead>
    <tbody>
      <tr class="section-band"><td colspan="3">Cotton</td></tr>
      <tr class="scent-row" style="height:44px"><td class="scent-name">Bamboo &amp; Hemp</td><td class="scent-code">BAM</td><td class="scent-notes">Bamboo stalks are complimented with natural vetiver and patchouli with undertones of hemp seed and oakmoss.</td></tr>

      <tr class="section-band"><td colspan="3">Floral</td></tr>
      <tr class="scent-row" style="height:102px"><td class="scent-name">Cherry Blossom</td><td class="scent-code">CHB</td><td class="scent-notes">Cherry Blossoms is a lovely shade of pink and smells just as fresh and delightful as Cherry Blossom trees in the Spring. It is citrusy, with fruity green top notes with floral middle notes of Rose, Lily of the Valley and Jasmine enhanced with long lasting sweet, woody and musk bottom notes.</td></tr>
      <tr class="scent-row" style="height:43px"><td class="scent-name">Tropic Petals</td><td class="scent-code">TRO</td><td class="scent-notes">Soak your worries away with the tropical blooms of verbena, bergamot, pear and lime and the final nodes of white ginger.</td></tr>
      <tr class="scent-row" style="height:82px"><td class="scent-name">Lilac</td><td class="scent-code">LIL</td><td class="scent-notes">Picture yourself driving down a winding country road with your windows down in the springtime. An alluring grove of lilac blossoms, rose, honeysuckle, jasmine, and lily of the vally will take you right down this memory lane.</td></tr>
      <tr class="scent-row" style="height:43px"><td class="scent-name">Gentle Grace</td><td class="scent-code">GEN</td><td class="scent-notes">Pure white grace fills the room with wafts of hyacinth and citrus, reminiscent of a bride's bouquet.</td></tr>

      <tr class="section-band"><td colspan="3">Specialty</td></tr>
      <tr class="scent-row" style="height:62px"><td class="scent-name">Cellar Special</td><td class="scent-code">CEL</td><td class="scent-notes">Our signature candle is an aromatic blend of freshly cut apples, juicy oranges, spicy and rich cinnamon, orange clove and colorful cranberries.</td></tr>
      <tr class="scent-row" style="height:62px"><td class="scent-name">Mischief Mix</td><td class="scent-code">MIS</td><td class="scent-notes">Mischief Mix is a wonderful purple candle. It will take you back to Saturday morning cartoons enjoyed with a big bowl of fruity cereal.</td></tr>
      <tr class="scent-row" style="height:102px"><td class="scent-name">Grandpa's Stoop</td><td class="scent-code">GPS</td><td class="scent-notes">Do you remember Grandpa sitting on his stoop with a pipe in his hand telling all the kids stories of the old days? That sweet pipe tobacco smelled so yummy!! Reminisce with our new Grandpa's Stoop candle that perfectly captures that aroma and will send you back in time.</td></tr>
      <tr class="scent-row" style="height:43px"><td class="scent-name">Patchouili</td><td class="scent-code">PAT</td><td class="scent-notes">Musky, woodsy, spicy and sweet, patchouli will relax yet uplift you at the same time.</td></tr>
      <tr class="scent-row" style="height:82px"><td class="scent-name">Ember Glow</td><td class="scent-code">EMB</td><td class="scent-notes">You know that feeling when a guy walks by and it's all you can do to not spin on your heels just to see where that divine scent came from? That's what Ember Glow, our new beautiful shade of gray candle, smells like!!</td></tr>

      <tr class="section-band"><td colspan="3">Refreshing</td></tr>
      <tr class="scent-row" style="height:46px"><td class="scent-name">Macadamia Nut Coffee</td><td class="scent-code">COF</td><td class="scent-notes">Start your day off right with the rich aroma of Australian macadamia nut, cocoa, and vanilla bean.</td></tr>
      <tr class="scent-row" style="height:62px"><td class="scent-name">Morning Roast</td><td class="scent-code">MRN</td><td class="scent-notes">Love the rich aroma of roasted coffee beans, without actually drinking the coffee? Skip the cream and sugar, and melt away with Morning Roast.</td></tr>
      <tr class="scent-row" style="height:62px"><td class="scent-name">Cool Refresher</td><td class="scent-code">REF</td><td class="scent-notes">Love the rich aroma of roasted coffee beans, without actually drinking the coffee? Skip the cream and sugar, and melt away with Morning Roast.</td></tr>
      <tr class="scent-row" style="height:82px"><td class="scent-name">Salted Caramel</td><td class="scent-code">SAL</td><td class="scent-notes">Adulthood meets childhood. The rich, smooth buttery flavors of your favorite childhood caramel, with the final nodes of sea salt that add that final blend of sweet and salty. All without the calories you'd expect!</td></tr>
    </tbody>
  </table>
</main>

</body>
</html>
```